PHVR (Harborview Stomach Wellness Collective of Ridgeford)

We need a business card design for a new medical group that specializes in Gastroenterology (digestive diseases). We need a double sided card that is professional yet modern.
The front would incorporate our logo, names, titles and contact info. In the back we would like a map to our office as well as a space to write a follow up appointment.
Our address is:
4172 E. Marlow Ave, Suite 118, Las Vegas, NV 89147
phone: (702) 555-0172
fax: (702) 555-0139
website: www.quillbrookclinic.example
Target Market(s)
Physicians and patients
Industry/Entity Type
Medical
Contact Information for Business Card
Name
Title
phone: (702) 555-0172
fax: (702) 555-0139

```html
<!DOCTYPE html>
<html lang="en">
<head>
<meta charset="utf-8">
<title>PHVR Business Card – Front and Back</title>
<link rel="stylesheet" href="https://fonts.googleapis.com/css2?family=Open+Sans:ital,wght@0,400;0,600;0,700;1,600&display=swap">
<style>
  :root {
    --bg: #8c8c8c;
    --card: #ffffff;
    --band-grey: #f3f1f2;
    --blue: #1d4fa3;
    --blue-dark: #133a80;
    --blue-light: #2f6fd3;
    --black: #0d0d0d;
    --grey-text: #8a8a8a;
    --ink: #222222;
    --map: #e6e6e6;
    --map-line: #bdbdbd;
  }
  * { box-sizing: border-box; margin: 0; padding: 0; }
  html, body { width: 1200px; height: 900px; overflow: hidden; }
  body {
    background: var(--bg);
    font-family: "Open Sans", Arial, sans-serif;
    position: relative;
  }
  .card {
    position: absolute;
    left: 250px;
    width: 700px;
    height: 400px;
    background: var(--card);
    overflow: hidden;
    box-shadow: 0 6px 18px rgba(0,0,0,0.25);
  }
  .card--front { top: 30px; }
  .card--back { top: 470px; }

  .card__bands {
    position: absolute; left: 0; right: 0; bottom: 0; height: 70px;
  }
  .band { position: absolute; left: 0; right: 0; }
  .band--thin-blue { top: 0; height: 10px; background: linear-gradient(90deg, var(--blue-dark), var(--blue-light), var(--blue-dark)); }
  .band--black { top: 10px; height: 18px; background: var(--black); }
  .band--blue { top: 28px; bottom: 0; background: linear-gradient(90deg, var(--blue-dark), var(--blue-light) 50%, var(--blue-dark)); }

  /* Front */
  .front__grey {
    position: absolute; left: 0; right: 0; top: 190px; bottom: 70px;
    background: var(--band-grey);
  }
  .brand {
    position: absolute; left: 40px; top: 90px;
    display: flex; align-items: center; gap: 16px;
  }
  .brand__mark {
    font-weight: 700; font-size: 62px; letter-spacing: 1px;
    color: var(--blue); line-height: 1;
  }
  .brand__divider { width: 2px; height: 76px; background: #b5b5b5; }
  .brand__name {
    font-weight: 600; font-size: 12.5px; line-height: 1.15;
    color: var(--grey-text); text-transform: uppercase; letter-spacing: 0.5px;
    width: 190px;
  }
  .person {
    position: absolute; right: 40px; top: 84px; text-align: right;
  }
  .person__name { font-weight: 700; font-size: 19px; color: var(--blue); letter-spacing: 0.5px; }
  .person__title { font-size: 16px; color: var(--ink); }

  .address {
    position: absolute; left: 38px; top: 212px;
    display: flex; gap: 8px; font-size: 15px; line-height: 1.6; color: var(--ink);
  }
  .address svg { flex: none; margin-top: 4px; }
  .contact {
    position: absolute; right: 40px; top: 244px;
    list-style: none; font-size: 16px; color: var(--ink); line-height: 1.5;
  }
  .contact li { display: flex; justify-content: flex-end; align-items: center; gap: 10px; }
  .contact svg { flex: none; }

  /* Back */
  .map {
    position: absolute; left: 210px; top: 22px; width: 300px; height: 100px;
    background: linear-gradient(180deg, var(--map), #d9d9d9);
    border: 1px solid var(--map-line);
  }
  .appointment {
    position: absolute; left: 0; right: 0; top: 132px; text-align: center;
    font-weight: 700; font-size: 22px; color: var(--blue);
  }
  .fields { position: absolute; left: 70px; right: 70px; top: 176px; font-size: 15px; color: var(--ink); }
  .field-row { display: flex; align-items: baseline; gap: 6px; margin-bottom: 16px; }
  .field-row .label { flex: none; }
  .field-row .dots { flex: 1; border-bottom: 2px dotted #555; height: 1px; }
  .notice {
    position: absolute; left: 0; right: 0; top: 286px; text-align: center;
    font-style: italic; font-weight: 600; font-size: 15px; color: var(--blue);
  }
</style>
</head>
<body>

<section class="card card--front" aria-label="Business card front">
  <div class="front__grey"></div>

  <div class="brand">
    <span class="brand__mark">PHVR</span>
    <span class="brand__divider"></span>
    <span class="brand__name">Harborview Stomach Wellness Collective of Ridgeford</span>
  </div>

  <div class="person">
    <div class="person__name">MARCUS DELANEY</div>
    <div class="person__title">Managing Director</div>
  </div>

  <div class="address">
    <svg width="11" height="15" viewBox="0 0 12 16" aria-hidden="true"><path d="M6 0a6 6 0 0 0-6 6c0 4.5 6 10 6 10s6-5.5 6-10a6 6 0 0 0-6-6zm0 8.5A2.5 2.5 0 1 1 6 3.5a2.5 2.5 0 0 1 0 5z" fill="var(--blue)"/></svg>
    <p>4172 E. Marlow Ave,<br>Suite 118, Las Vegas,<br>NV 89147</p>
  </div>

  <ul class="contact">
    <li>(702) 555-0172
      <svg width="16" height="14" viewBox="0 0 16 14" aria-hidden="true"><path d="M1 5c0-3 14-3 14 0v1h-4V4H5v2H1z M3 7h10l2 6H1z" fill="var(--blue)"/></svg>
    </li>
    <li>(702) 555-0139
      <svg width="16" height="14" viewBox="0 0 16 14" aria-hidden="true"><rect x="1" y="4" width="14" height="10" rx="1" fill="var(--blue)"/><rect x="4" y="0" width="8" height="5" fill="var(--blue)"/><rect x="4" y="7" width="8" height="4" fill="#fff"/></svg>
    </li>
    <li>www.quillbrookclinic.example
      <svg width="16" height="14" viewBox="0 0 16 14" aria-hidden="true"><g fill="none" stroke="var(--blue)" stroke-width="2"><rect x="1" y="6" width="8" height="5" rx="2.5" transform="rotate(-35 5 8.5)"/><rect x="7" y="3" width="8" height="5" rx="2.5" transform="rotate(-35 11 5.5)"/></g></svg>
    </li>
  </ul>

  <div class="card__bands">
    <div class="band band--thin-blue"></div>
    <div class="band band--black"></div>
    <div class="band band--blue"></div>
  </div>
</section>

<section class="card card--back" aria-label="Business card back">
  <div class="map" role="img" aria-label="Street map showing the route to the office"></div>

  <h2 class="appointment">Your Next Appointment is</h2>

  <div class="fields">
    <div class="field-row"><span class="label">Name :</span><span class="dots"></span></div>
    <div class="field-row">
      <span class="label">Date :</span><span class="dots"></span>
      <span class="label">Time :</span><span class="dots"></span>
    </div>
  </div>

  <p class="notice">If unable to keep appointment, kindly give 24hrs notice.</p>

  <div class="card__bands">
    <div class="band band--thin-blue"></div>
    <div class="band band--black"></div>
    <div class="band band--blue"></div>
  </div>
</section>

</body>
</html>
```